WordPress Website for Accounting Firm

I have attached an excel sheet showing what i need done for my accounting website. Currently i have a WP website but its not live and do not like it. I can give a link if that will help. Total pages is around 12. I can buy and supply the images but have provided indication of what i want in the excel. I will need the designer to do the coding to make the website fully functional. I want a clean look and attractive. Don't want too dark colors. Once i like the landing page, i will need the designer to code code the website. Just want to look first. I will provide the logo file and put the contents myself. Just put dummy contents for now to show how it will look.
Updates
Can you please use the attached images so i can see how nit will look on the coverage as an option. These are from pixelharbor
264918053
418273596
1537206419
1096382147
Currently there are only 2 provided by myself as Photo 1 and Photo 2
Many Thanks!
Industry/Entity Type
Accounting and Finance
Number of Pages Required
5+ page

```html
<!DOCTYPE html>
<html lang="en">
<head>
<meta charset="utf-8">
<title>Ledgerline Advisory – Accounting and Tax Advisors</title>
<link rel="stylesheet" href="https://fonts.googleapis.com/css2?family=Poppins:wght@300;400;500;600;700&display=swap">
<style>
:root{
  --green:#4c9a3c;
  --green-dark:#3f8632;
  --ink:#2b2b2b;
  --muted:#6f6f6f;
  --soft:#f3f4f6;
  --footer:#3d3d47;
  --white:#ffffff;
  --star:#b9d11b;
}
*{box-sizing:border-box;margin:0;padding:0}
html,body{width:1200px;height:3646px;overflow:hidden}
body{font-family:'Poppins',sans-serif;color:var(--ink);background:var(--white);position:relative}
.abs{position:absolute}
.topbar{left:0;top:0;width:1200px;height:37px;background:var(--green);color:var(--white);font-size:14px}
.topbar .contact{position:absolute;top:9px;display:flex;align-items:center;gap:8px}
.topbar .mail{left:800px}
.topbar .phone{left:1028px;font-weight:600}
.header{left:0;top:37px;width:1200px;height:60px;background:var(--white)}
.brand{position:absolute;left:60px;top:6px;display:flex;align-items:center;gap:12px}
.brand .dot{width:46px;height:46px;border-radius:50%;border:4px solid var(--green)}
.brand span{font-size:14px;font-weight:500;color:var(--ink);letter-spacing:.3px}
.nav{position:absolute;right:62px;top:21px;display:flex;gap:26px;font-size:13px;text-transform:uppercase}
.nav a{color:var(--ink);text-decoration:none}
.nav a.active{color:var(--green)}
.hero{left:0;top:97px;width:1200px;height:563px;background:linear-gradient(100deg,#8e8a74 0%,#b9b6a8 30%,#5e7f86 58%,#2f4a54 80%,#cfd3d2 100%)}
.hero-disc{left:61px;top:135px;width:486px;height:486px;border-radius:50%;background:var(--green);color:var(--white);text-align:center;padding-top:74px}
.hero-disc h1{font-size:37px;font-weight:600;line-height:48px;letter-spacing:.3px}
.hero-disc p{font-size:13.5px;line-height:22px;margin:16px auto 0;width:370px}
.btn-light{display:inline-block;margin-top:18px;background:var(--white);color:var(--ink);font-size:13px;padding:9px 16px;border-radius:20px}
.about-bg{left:0;top:660px;width:1200px;height:427px;background:var(--soft)}
.about-box{left:57px;top:722px;width:1086px;height:304px;border:3px solid var(--green);border-radius:28px;background:var(--white)}
.about-text{left:107px;top:780px;width:530px;font-size:13.3px;line-height:22.5px;color:var(--muted)}
.btn-green{display:inline-block;background:var(--green);color:var(--white);font-size:12.5px;padding:7px 17px;border-radius:18px;text-transform:uppercase}
.about-btn{left:104px;top:922px}
.eyebrow{font-size:13px;color:var(--ink);display:flex;align-items:center;gap:8px}
.eyebrow::before{content:"";width:14px;height:1px;background:var(--muted)}
.about-eyebrow{left:680px;top:785px}
.about-title{left:704px;top:822px;width:360px;font-size:23px;line-height:34px;font-weight:600;color:var(--green)}
.why-eyebrow{left:60px;top:1169px}
.why-title{left:60px;top:1192px;font-size:25px;font-weight:600;color:var(--green)}
.why-list{left:58px;top:1253px;width:610px;list-style:none;font-size:13.3px;line-height:20px}
.why-list li{display:flex;gap:18px;margin-bottom:8.6px}
.why-list svg{flex:none;margin-top:1px}
.why-photo{left:740px;top:1186px;width:396px;height:396px;border-radius:50%;border:4px solid var(--green);background:linear-gradient(135deg,#e9eef3,#b8c7d8 45%,#5d7ea6 75%,#2b3c58)}
.why-badge{left:692px;top:1413px;width:136px;height:136px;border-radius:50%;background:var(--green);color:var(--white);font-weight:600;font-size:16px;line-height:20px;text-align:center;padding-top:37px}
.testi-bg{left:0;top:1670px;width:1200px;height:402px;background:linear-gradient(90deg,#a69a8a,#e4e0d9 30%,#f2f1ee 55%,#d0d6de 80%,#6f7c8e)}
.testi-eyebrow{left:467px;top:1721px}
.testi-title{left:467px;top:1745px;font-size:25px;font-weight:600;color:var(--green)}
.card{top:1808px;width:340px;height:194px;background:var(--white);border-radius:4px;padding:26px 20px 0 20px}
.card .avatar{position:absolute;left:22px;top:26px;width:60px;height:60px;border-radius:50%;border:2px solid var(--green);background:linear-gradient(160deg,#e8d6c8,#b58c74)}
.card .quote{position:absolute;right:0;top:0;width:44px;height:44px;background:var(--green);border-radius:0 4px 0 12px;color:var(--white);font-size:38px;font-weight:700;line-height:58px;text-align:center}
.card .stars{position:absolute;left:98px;top:30px;display:flex;gap:3px}
.card .who{position:absolute;left:98px;top:50px;font-size:13.5px}
.card .who b{color:var(--green);font-weight:600;margin-right:6px}
.card p{position:absolute;left:20px;top:92px;width:305px;font-size:12.5px;line-height:22.5px;color:var(--muted)}
.arrow{width:38px;height:38px;border-radius:50%;display:flex;align-items:center;justify-content:center;top:1894px}
.ind-eyebrow{left:450px;top:2161px}
.ind-title{left:0;top:2186px;width:1200px;text-align:center;font-size:25px;font-weight:600;color:var(--green)}
.ind{width:252px;height:259px;border-radius:14px;overflow:hidden;background:var(--green)}
.ind .ph{height:216px}
.ind .label{height:43px;color:var(--white);font-size:16px;font-weight:600;text-align:center;line-height:44px}
.see-more{left:581px;top:2861px;width:107px;height:36px;border:2px solid var(--green);border-radius:18px;font-size:12.5px;text-align:center;line-height:32px;text-transform:uppercase}
.news-box{left:57px;top:2981px;width:1086px;height:274px;border:3px solid var(--green);border-radius:28px;text-align:center}
.news-box h2{margin-top:42px;font-size:25px;font-weight:600;color:var(--green)}
.news-box p{width:600px;margin:6px auto 0;font-size:12.3px;line-height:15px;color:var(--muted)}
.fields{display:flex;gap:16px;justify-content:center;margin-top:34px}
.field{width:302px;height:38px;border:1px solid #9a9a9a;border-radius:20px;text-align:left;padding:9px 16px;font-size:13px;color:var(--muted)}
.news-btn{margin-top:30px;padding:8px 16px}
.footer{left:0;top:3339px;width:1200px;height:307px;background:var(--footer);color:var(--white)}
.foot-brand{position:absolute;left:483px;top:50px;display:flex;align-items:center;gap:12px}
.foot-brand .dot{width:54px;height:54px;border-radius:50%;border:4px solid var(--white)}
.foot-brand span{font-size:14px;font-weight:500}
.foot-item{position:absolute;top:158px;width:260px;text-align:center;font-size:12.5px;line-height:21px}
.foot-item .ic{width:38px;height:38px;border-radius:50%;margin:0 auto 14px;display:flex;align-items:center;justify-content:center;border:2px solid var(--green)}
.foot-item .ic.fill{background:var(--green)}
</style>
</head>
<body>

<div class="abs topbar">
  <div class="contact mail">
    <svg width="24" height="18" viewBox="0 0 24 18"><rect x="1" y="1" width="22" height="16" fill="none" stroke="#fff" stroke-width="2"/><path d="M1 1l11 9 11-9" fill="none" stroke="#fff" stroke-width="2"/></svg>
    info@ledgerline.co.nz
  </div>
  <div class="contact phone">
    <svg width="18" height="18" viewBox="0 0 24 24"><path d="M6.6 10.8a15 15 0 0 0 6.6 6.6l2.2-2.2c.3-.3.7-.4 1-.2 1.1.4 2.3.6 3.6.6.6 0 1 .4 1 1V20c0 .6-.4 1-1 1A17 17 0 0 1 3 4c0-.6.4-1 1-1h3.5c.6 0 1 .4 1 1 0 1.3.2 2.5.6 3.6.1.3 0 .7-.2 1z" fill="#fff"/></svg>
    021 555 0147
  </div>
</div>

<header class="abs header">
  <div class="brand"><div class="dot"></div><span>LEDGERLINE ADVISORY</span></div>
  <nav class="nav">
    <a class="active" href="#">Home</a><a href="#">Solutions</a><a href="#">Clients</a><a href="#">Contact Us</a><a href="#">Client Resources</a>
  </nav>
</header>

<section class="abs hero" role="img" aria-label="Photo of a smiling businessman in a suit talking on the phone at his laptop"></section>
<div class="abs hero-disc">
  <h1>LEDGERLINE<br>ADVISORY<br>ACCOUNTING AND<br>TEX ADVISORS</h1>
  <p>Lorem Ipsum is simply dummy text of the printing and typesetting industry.Lorem Ipsum has been the industry's standard dummy text ever since the 1500s,</p>
  <span class="btn-light">CONTACT US TODAY</span>
</div>

<div class="abs about-bg"></div>
<div class="abs about-box"></div>
<p class="abs about-text">Lorem Ipsum is simply dummy text of the printing and typesetting industry. Lorem Ipsumhas been the industry's standard dummy text ever since the 1500s, when an unknown printer took a galley of type and scrambled it to make a type specimen book. It has survived not only five centuries, but also the leap into electronic typesetting, remaining essentially unchanged.</p>
<span class="abs btn-green about-btn">More Aubout Us</span>
<div class="abs eyebrow about-eyebrow">Welcome To Our Company</div>
<h2 class="abs about-title">We Do Accounting Firm Ledgerline Advisory And Tex Advisors.</h2>

<div class="abs eyebrow why-eyebrow">Solutions</div>
<h2 class="abs why-title">Why Choose Us</h2>
<ul class="abs why-list">
  <li><svg width="18" height="18" viewBox="0 0 18 18"><circle cx="9" cy="9" r="7.5" fill="none" stroke="#4c9a3c" stroke-width="1.6"/><path d="M5 9l3 3 6-7" fill="none" stroke="#4c9a3c" stroke-width="2"/></svg>We specialise accounting and tax solutions for all business structures and industries.</li>
  <li><svg width="18" height="18" viewBox="0 0 18 18"><circle cx="9" cy="9" r="7.5" fill="none" stroke="#4c9a3c" stroke-width="1.6"/><path d="M5 9l3 3 6-7" fill="none" stroke="#4c9a3c" stroke-width="2"/></svg>Our Team are qualified professionals with 50+ years of combined experience in CA industry.</li>
  <li><svg width="18" height="18" viewBox="0 0 18 18"><circle cx="9" cy="9" r="7.5" fill="none" stroke="#4c9a3c" stroke-width="1.6"/><path d="M5 9l3 3 6-7" fill="none" stroke="#4c9a3c" stroke-width="2"/></svg>We are Accessable 7 days a week.</li>
  <li><svg width="18" height="18" viewBox="0 0 18 18"><circle cx="9" cy="9" r="7.5" fill="none" stroke="#4c9a3c" stroke-width="1.6"/><path d="M5 9l3 3 6-7" fill="none" stroke="#4c9a3c" stroke-width="2"/></svg>We constancy upskill to keep up with changes to tax laws and legislation</li>
  <li><svg width="18" height="18" viewBox="0 0 18 18"><circle cx="9" cy="9" r="7.5" fill="none" stroke="#4c9a3c" stroke-width="1.6"/><path d="M5 9l3 3 6-7" fill="none" stroke="#4c9a3c" stroke-width="2"/></svg>Our adadvise is explained in plain english so you understand</li>
  <li><svg width="18" height="18" viewBox="0 0 18 18"><circle cx="9" cy="9" r="7.5" fill="none" stroke="#4c9a3c" stroke-width="1.6"/><path d="M5 9l3 3 6-7" fill="none" stroke="#4c9a3c" stroke-width="2"/></svg>Our fees are not only fair but very competitive</li>
  <li><svg width="18" height="18" viewBox="0 0 18 18"><circle cx="9" cy="9" r="7.5" fill="none" stroke="#4c9a3c" stroke-width="1.6"/><path d="M5 9l3 3 6-7" fill="none" stroke="#4c9a3c" stroke-width="2"/></svg>We don't believe in one size fits all, we listen to client's challenges indiviually</li>
  <li><svg width="18" height="18" viewBox="0 0 18 18"><circle cx="9" cy="9" r="7.5" fill="none" stroke="#4c9a3c" stroke-width="1.6"/><path d="M5 9l3 3 6-7" fill="none" stroke="#4c9a3c" stroke-width="2"/></svg>Our lavel of service and work ethics is no different to any other large CA practices</li>
  <li><svg width="18" height="18" viewBox="0 0 18 18"><circle cx="9" cy="9" r="7.5" fill="none" stroke="#4c9a3c" stroke-width="1.6"/><path d="M5 9l3 3 6-7" fill="none" stroke="#4c9a3c" stroke-width="2"/></svg>We have affiliations other business partners</li>
  <li><svg width="18" height="18" viewBox="0 0 18 18"><circle cx="9" cy="9" r="7.5" fill="none" stroke="#4c9a3c" stroke-width="1.6"/><path d="M5 9l3 3 6-7" fill="none" stroke="#4c9a3c" stroke-width="2"/></svg>We keep up with everchanging cloud based technology</li>
</ul>
<div class="abs why-photo" role="img" aria-label="Photo of a smiling office worker on the phone with colleagues gathered around his desk"></div>
<div class="abs why-badge">20+<br>Years<br>Experience</div>

<section class="abs testi-bg" role="img" aria-label="Blurred photo of business people reviewing documents at a desk"></section>
<div class="abs eyebrow testi-eyebrow">Testimonials</div>
<h2 class="abs testi-title">What Our Client Says</h2>

<div class="abs card" style="left:59px">
  <div class="avatar" role="img" aria-label="Client portrait"></div>
  <div class="quote">“</div>
  <div class="stars"><svg width="82" height="14" viewBox="0 0 82 14"><g fill="#b9d11b"><path id="s" d="M7 0l2 4.6 5 .4-3.8 3.3 1.2 4.9L7 10.6 2.6 13.2 3.8 8.3 0 5l5-.4z"/><use href="#s" x="17"/><use href="#s" x="34"/><use href="#s" x="51"/><use href="#s" x="68"/></g></svg></div>
  <div class="who"><b>Marcus Hale</b>Tx Manager</div>
  <p>Lorem Ipsum is simply dummy text of the printing and typesetting industry. Lorem Ipsumhas been the industry's standard dummy text ever since the 1500s,</p>
</div>
<div class="abs card" style="left:430px">
  <div class="avatar" role="img" aria-label="Client portrait" style="background:linear-gradient(160deg,#c9d3e0,#3d4f6a)"></div>
  <div class="quote">“</div>
  <div class="stars"><svg width="82" height="14" viewBox="0 0 82 14"><g fill="#b9d11b"><use href="#s"/><use href="#s" x="17"/><use href="#s" x="34"/><use href="#s" x="51"/><use href="#s" x="68"/></g></svg></div>
  <div class="who"><b>Marcus Hale</b>Tx Manager</div>
  <p>Lorem Ipsum is simply dummy text of the printing and typesetting industry. Lorem Ipsumhas been the industry's standard dummy text ever since the 1500s,</p>
</div>
<div class="abs card" style="left:801px">
  <div class="avatar" role="img" aria-label="Client portrait" style="background:linear-gradient(160deg,#f1e6d6,#cfae86)"></div>
  <div class="quote">“</div>
  <div class="stars"><svg width="82" height="14" viewBox="0 0 82 14"><g fill="#b9d11b"><use href="#s"/><use href="#s" x="17"/><use href="#s" x="34"/><use href="#s" x="51"/><use href="#s" x="68"/></g></svg></div>
  <div class="who"><b>Marcus Hale</b>Tx Manager</div>
  <p>Lorem Ipsum is simply dummy text of the printing and typesetting industry. Lorem Ipsumhas been the industry's standard dummy text ever since the 1500s,</p>
</div>
<div class="abs arrow" style="left:31px;background:var(--green)"><svg width="12" height="16" viewBox="0 0 12 16"><path d="M9 2L3 8l6 6" fill="none" stroke="#fff" stroke-width="2.4"/></svg></div>
<div class="abs arrow" style="left:1130px;background:#fff"><svg width="12" height="16" viewBox="0 0 12 16"><path d="M3 2l6 6-6 6" fill="none" stroke="#222" stroke-width="2.4"/></svg></div>

<div class="abs eyebrow ind-eyebrow">Services</div>
<h2 class="abs ind-title">Industries We Represent</h2>

<div class="abs ind" style="left:59px;top:2260px"><div class="ph" role="img" aria-label="Photo of a doctor and nurse reviewing a tablet" style="background:linear-gradient(135deg,#e4ebf1,#9fb4c6 60%,#5aa7b9)"></div><div class="label">Healthcare Specialists</div></div>
<div class="abs ind" style="left:337px;top:2260px"><div class="ph" role="img" aria-label="Photo of construction workers shaking hands on site" style="background:linear-gradient(135deg,#d9e2ec,#e07a3a 45%,#4d5563)"></div><div class="label">Construction</div></div>
<div class="abs ind" style="left:616px;top:2260px"><div class="ph" role="img" aria-label="Photo of two businessmen working at a laptop" style="background:linear-gradient(135deg,#f1f2f4,#8f9aa8 55%,#2e3746)"></div><div class="label">Professional Services</div></div>
<div class="abs ind" style="left:889px;top:2260px"><div class="ph" role="img" aria-label="Photo of a hand signing a legal document" style="background:linear-gradient(135deg,#3b4250,#9aa0a8 50%,#e8e8e6)"></div><div class="label">Legal</div></div>

<div class="abs ind" style="left:59px;top:2550px"><div class="ph" role="img" aria-label="Photo of two contractors in hard hats with plans" style="background:linear-gradient(135deg,#c8d3de,#e3893d 55%,#5b6370)"></div><div class="label">Contractors</div></div>
<div class="abs ind" style="left:337px;top:2550px"><div class="ph" role="img" aria-label="Photo of a house model on architectural drawings" style="background:linear-gradient(135deg,#f4f5f6,#c9d3dc 55%,#8da2b5)"></div><div class="label">Architecture</div></div>
<div class="abs ind" style="left:616px;top:2550px"><div class="ph" role="img" aria-label="Photo of shoppers at a retail store counter" style="background:linear-gradient(135deg,#6a6258,#b8a58c 50%,#3d3a36)"></div><div class="label">Retail</div></div>
<div class="abs ind" style="left:889px;top:2550px"><div class="ph" role="img" aria-label="Photo of medical practitioners in masks with a tablet" style="background:linear-gradient(135deg,#f3f1ee,#dcd6d0 55%,#9aa4ae)"></div><div class="label">Medical Practiniors</div></div>

<div class="abs see-more">See More</div>

<section class="abs news-box">
  <h2>Subscribe Our Newsletter</h2>
  <p>Lorem Ipsum is simply dummy text of the printing and typesetting industry. Lorem Ipsum has been the industry's standard dummy text ever since the 1500s,</p>
  <div class="fields"><div class="field">Your Name</div><div class="field">Your E-mail</div></div>
  <span class="btn-green news-btn">Subscribe</span>
</section>

<footer class="abs footer">
  <div class="foot-brand"><div class="dot"></div><span>LEDGERLINE ADVISORY</span></div>
  <div class="foot-item" style="left:167px">
    <div class="ic fill"><svg width="16" height="20" viewBox="0 0 16 20"><path d="M8 1a6 6 0 0 0-6 6c0 4.5 6 11 6 11s6-6.5 6-11a6 6 0 0 0-6-6z" fill="none" stroke="#fff" stroke-width="2"/><circle cx="8" cy="7" r="2" fill="#fff"/></svg></div>
    P O Box 10482, Greenhill, Auckland 2010
  </div>
  <div class="foot-item" style="left:383px">
    <div class="ic"><svg width="16" height="16" viewBox="0 0 24 24"><path d="M6.6 10.8a15 15 0 0 0 6.6 6.6l2.2-2.2c.3-.3.7-.4 1-.2 1.1.4 2.3.6 3.6.6.6 0 1 .4 1 1V20c0 .6-.4 1-1 1A17 17 0 0 1 3 4c0-.6.4-1 1-1h3.5c.6 0 1 .4 1 1 0 1.3.2 2.5.6 3.6.1.3 0 .7-.2 1z" fill="#fff"/></svg></div>
    <b style="font-weight:600">021 555 0147</b>
  </div>
  <div class="foot-item" style="left:603px">
    <div class="ic"><svg width="18" height="14" viewBox="0 0 24 18"><rect x="1" y="1" width="22" height="16" fill="none" stroke="#fff" stroke-width="2"/><path d="M1 1l11 9 11-9" fill="none" stroke="#fff" stroke-width="2"/></svg></div>
    info@ledgerline.co.nz<br>accounts@ledgerline.co.nz
  </div>
  <div class="foot-item" style="left:824px">
    <div class="ic"><svg width="18" height="18" viewBox="0 0 20 20"><circle cx="10" cy="10" r="8" fill="none" stroke="#fff" stroke-width="1.6"/><ellipse cx="10" cy="10" rx="3.5" ry="8" fill="none" stroke="#fff" stroke-width="1.4"/><path d="M2 10h16M3.5 6h13M3.5 14h13" stroke="#fff" stroke-width="1.2"/></svg></div>
    ledgerline.co.nz
  </div>
</footer>

</body>
</html>
```